A start up special flyer design!

Hi All - Have updated the attachment content - This is the info required for the designs.
I need a catchy flyer to send out to a few areas to advertise the start of my plumbing business!
The flyer will contain an offer for customers, which will need to have some key details on it. See attached. Feel free to fit these criteria into the flyer given your knowledge on design and messaging principles. Key thing to get across to customers is the discount and special offer, and that it is a start up offer.
I have a logo that needs to be on the flyer as well - let me know what format you require and I will send through to you.
The color scheme needs to be blue / grey / black / white.
Let me know if you have any questions.
I

```html
<!DOCTYPE html>
<html lang="en">
<head>
<meta charset="utf-8">
<title>Marlow Pipe Plumbing – Start-up Offer Flyer</title>
<link rel="stylesheet" href="https://fonts.googleapis.com/css2?family=Anton&family=Montserrat:wght@500;600;700;800&display=swap">
<style>
  :root{
    --blue:#1f7fd9;
    --sky:#2a86e0;
    --red:#e3202a;
    --yellow:#ffe600;
    --ink:#111111;
    --paper:#ffffff;
    --mist:#d9dcdf;
  }
  *{margin:0;padding:0;box-sizing:border-box}
  html,body{width:857px;height:1200px;overflow:hidden;background:var(--paper)}
  .flyer{
    position:relative;width:857px;height:1200px;overflow:hidden;
    background:linear-gradient(180deg,var(--sky) 0%,#7db6ec 22%,#eef4fa 38%,#ffffff 48%,#ffffff 70%,var(--mist) 100%);
    font-family:"Montserrat",Arial,sans-serif;
  }
  .hero-photo{
    position:absolute;left:0;top:0;width:857px;height:410px;
    background:radial-gradient(ellipse at 52% 40%,#eef3f6 0%,#c9dce9 30%,#8fb6d6 55%,rgba(120,170,220,0) 75%);
  }
  .offer{position:absolute;left:455px;top:582px;width:400px;height:380px;z-index:1}
  .offer text{font-family:"Montserrat",Arial,sans-serif}
  .headline{position:absolute;left:0;top:0;width:857px;height:680px;z-index:2}
  .headline text{font-family:"Anton",Impact,sans-serif;paint-order:stroke fill;stroke-linejoin:round}
  .brand{
    position:absolute;left:48px;top:762px;display:flex;align-items:center;gap:12px;white-space:nowrap;
  }
  .brand-dot{width:30px;height:30px;border-radius:50%;background:var(--blue);flex:none}
  .brand-name{font-weight:700;font-size:27px;letter-spacing:1px;color:var(--blue);line-height:1}
  .tagline{
    position:absolute;left:40px;top:840px;width:430px;text-align:center;
    color:var(--blue);font-weight:700;font-size:19px;line-height:1.25;
  }
  .booking{
    position:absolute;left:48px;top:900px;width:500px;
    color:var(--ink);font-weight:500;font-size:18px;line-height:1.25;
  }
  .phone-bar{
    position:absolute;left:47px;top:956px;width:782px;height:64px;border-radius:32px;
    background:var(--red);display:flex;align-items:center;padding:0 10px;
  }
  .phone-bar svg{flex:none}
  .phone-number{
    font-family:"Montserrat",Arial,sans-serif;font-weight:800;font-size:50px;color:var(--paper);
    letter-spacing:1px;margin-left:14px;line-height:1;flex:1;
  }
  .service-icons{display:flex;gap:6px}
  .web{
    position:absolute;left:0;top:1030px;width:857px;text-align:center;
    font-weight:800;font-size:33px;color:var(--ink);
  }
  .email{
    position:absolute;left:0;top:1073px;width:857px;text-align:center;
    font-weight:700;font-size:27px;color:var(--ink);
  }
  .accent-red{color:var(--red)}
  .accent-blue{color:var(--blue)}
  .terms{
    position:absolute;left:0;top:1118px;width:857px;text-align:center;
    font-weight:500;font-size:16px;color:var(--ink);line-height:1.45;
  }
</style>
</head>
<body>
<main class="flyer">
  <div class="hero-photo" role="img" aria-label="Photo of a plumber pulling open his shirt like a superhero to reveal a company t-shirt"></div>

  <svg class="offer" viewBox="0 0 400 380" aria-label="Get 20% off your overall bill, plus a free hot water heater health check and replacement quote">
    <circle cx="205" cy="190" r="172" fill="#fff"/>
    <circle cx="205" cy="190" r="164" fill="#e3202a"/>
    <g transform="rotate(-8 40 128)">
      <rect x="12" y="108" width="70" height="34" fill="#fff"/>
      <rect x="16" y="112" width="62" height="26" fill="#e3202a"/>
      <text x="47" y="133" text-anchor="middle" font-size="22" font-weight="800" fill="#fff">GET</text>
    </g>
    <text x="180" y="180" text-anchor="middle" font-size="135" fill="#fff"
          textLength="200" lengthAdjust="spacingAndGlyphs" style="font-family:Anton,Impact,sans-serif">20</text>
    <text x="318" y="112" text-anchor="middle" font-size="70" font-weight="800" fill="#fff">%</text>
    <text x="318" y="178" text-anchor="middle" font-size="46" fill="#fff" style="font-family:Anton,Impact,sans-serif">OFF</text>
    <text x="212" y="228" text-anchor="middle" font-size="20" font-weight="700" fill="#fff">YOUR OVERALL BILL*</text>
    <g transform="rotate(-8 72 256)">
      <rect x="36" y="242" width="74" height="30" fill="#fff"/>
      <rect x="40" y="246" width="66" height="22" fill="#e3202a"/>
      <text x="73" y="264" text-anchor="middle" font-size="18" font-weight="800" fill="#fff">PLUS</text>
    </g>
    <text text-anchor="middle" font-size="17" font-weight="700" fill="#ffe600">
      <tspan x="232" y="258">A FREE Hot Water</tspan>
      <tspan x="232" y="279">Heater Health Check</tspan>
      <tspan x="232" y="300">and Replacement</tspan>
      <tspan x="232" y="321">Quote**</tspan>
    </text>
  </svg>

  <svg class="headline" viewBox="0 0 857 680" aria-label="All plumbing problems Solved! Marlow saves the day!">
    <text x="414" y="340" text-anchor="middle" font-size="64" fill="#fff" stroke="#1f7fd9" stroke-width="10"
          textLength="600" lengthAdjust="spacingAndGlyphs" transform="rotate(-3 414 320)">All plumbing problems</text>
    <text x="418" y="552" text-anchor="middle" font-size="225" fill="#fff" stroke="#1f7fd9" stroke-width="14"
          textLength="690" lengthAdjust="spacingAndGlyphs" transform="rotate(-3 418 460)">Solved!</text>
    <text x="424" y="645" text-anchor="middle" font-size="80" fill="#e3202a" stroke="#fff" stroke-width="8"
          textLength="680" lengthAdjust="spacingAndGlyphs" transform="rotate(-3 424 615)">MARLOW SAVES THE DAY!</text>
  </svg>

  <div class="brand">
    <span class="brand-dot"></span>
    <span class="brand-name">MARLOW PIPE PLUMBING</span>
  </div>

  <p class="tagline">All plumbing, draining &amp; gas fitting<br>works at competitive prices!</p>
  <p class="booking">Call or email Marlow for an appointment now or<br>alternatively make a booking directly on our website</p>

  <div class="phone-bar">
    <svg width="58" height="58" viewBox="0 0 58 58" aria-label="Phone">
      <circle cx="29" cy="29" r="28" fill="#fff"/>
      <circle cx="29" cy="29" r="24" fill="#111"/>
      <path d="M16 26c0-6 26-6 26 0l-2 4-6-2v-3h-10v3l-6 2z" fill="#fff"/>
      <rect x="19" y="31" width="20" height="12" rx="2" fill="#fff"/>
    </svg>
    <span class="phone-number">0400 555 218</span>
    <div class="service-icons">
      <svg width="50" height="50" viewBox="0 0 50 50" aria-label="Pipes">
        <circle cx="25" cy="25" r="24" fill="#fff"/><circle cx="25" cy="25" r="20" fill="#111"/>
        <rect x="11" y="20" width="28" height="6" fill="#fff"/><rect x="22" y="14" width="6" height="20" fill="#fff"/>
      </svg>
      <svg width="50" height="50" viewBox="0 0 50 50" aria-label="Tap and drop">
        <circle cx="25" cy="25" r="24" fill="#fff"/><circle cx="25" cy="25" r="20" fill="#111"/>
        <rect x="12" y="16" width="22" height="6" fill="#fff"/><rect x="28" y="16" width="6" height="11" fill="#fff"/>
        <path d="M31 30c-3 4-3 7 0 7s3-3 0-7z" fill="#fff"/>
      </svg>
      <svg width="50" height="50" viewBox="0 0 50 50" aria-label="Gas flame">
        <circle cx="25" cy="25" r="24" fill="#fff"/><circle cx="25" cy="25" r="20" fill="#111"/>
        <path d="M25 12c6 7 9 11 9 16a9 9 0 0 1-18 0c0-4 3-6 4-9 1 3 2 4 3 4 0-4 1-7 2-11z" fill="#fff"/>
      </svg>
    </div>
  </div>

  <p class="web">www.<span class="accent-red">marlowpipe</span><span class="accent-blue">plumbing</span>.com</p>
  <p class="email">email: hello@<span class="accent-red">marlowpipe</span><span class="accent-blue">plumbing</span>.com</p>
  <p class="terms">*Offer expires 30 October 2016<br>**Quote valid for 12 months from the date of initial quotation</p>
</main>
</body>
</html>
```